aesthetic packaging for down comforter company

Hi guys,

I'm looking for a creative, aesthetic, serious, premium & luxury package design for a down comforter product. The box will be 50cm x 25cm x 25 cm.

please use our logo as reference to show how premium our product is

A small description of what is our product. It is a downcomforter blanket that caters to ALL-SEASONS. Size will be both Queen and King. So please add an option where it can be marked as one of the options.

It is a baffle box design. The product is DESIGNED IN AUSTRALIA, please add this key point

Down is a natural material and the higher the Down content, the lighter and softer the product. Down differs considerably from feathers, as it does not have the hard quill shafts that is common to feather. It is the fluffy filament which comes from the breast of a duck and is an extremely efficient natural insulator.

Target Market(s)

mothers,moms, ladies,girls

Requirements
Nice to have
• feathers, beds ,linen, anything to do with bedding if possible. Try to minimize pictures

```html
<!DOCTYPE html>
<html lang="en">
<head>
<meta charset="utf-8">
<title>Down Comforter Box – Dieline</title>
<link rel="stylesheet" href="https://fonts.googleapis.com/css2?family=Roboto+Condensed:wght@700&display=swap">
<style>
  :root {
    --paper: #ffffff;
    --cut-line: #3a3a3a;
    --gold: #b8944e;
    --lemon: #f3e600;
    --ink: #111111;
    --label: #ffffff;
    --quilt-light: #f4f4f4;
    --quilt-mid: #d9d9d9;
    --quilt-shade: #b9b9b9;
  }
  html, body {
    margin: 0;
    padding: 0;
    width: 1200px;
    height: 423px;
    overflow: hidden;
    background: var(--paper);
  }
  .dieline {
    display: block;
    width: 1200px;
    height: 423px;
    font-family: "Roboto Condensed", "Arial Narrow", sans-serif;
    font-weight: 700;
  }
  .cut { fill: none; stroke: var(--cut-line); stroke-width: 1; }
  .band-gold { fill: var(--gold); }
  .band-lemon { fill: var(--lemon); }
  .chevron-ink { fill: var(--ink); }
  .brand-mark { fill: var(--label); }
  .brand-name { fill: var(--label); font-size: 12px; letter-spacing: 1px; }
  .origin-note { fill: var(--label); font-size: 10px; }
  .company-field { fill: var(--ink); font-size: 11px; }
  .story {
    margin: 0;
    font-family: "Roboto Condensed", "Arial Narrow", sans-serif;
    font-weight: 700;
    font-size: 8px;
    line-height: 10px;
    color: var(--ink);
    text-align: justify;
  }
</style>
</head>
<body>
<svg class="dieline" viewBox="0 0 1500 529" xmlns="http://www.w3.org/2000/svg">
  <defs>
    <radialGradient id="quiltTone" cx="50%" cy="45%" r="65%">
      <stop offset="0%" stop-color="var(--quilt-light)"/>
      <stop offset="70%" stop-color="var(--quilt-mid)"/>
      <stop offset="100%" stop-color="var(--quilt-shade)"/>
    </radialGradient>
  </defs>

  <!-- Glue flap -->
  <path class="cut" d="M28 143 L4 150 L4 383 L28 390"/>

  <!-- Top flaps -->
  <path class="cut" d="M28 143 L30 60 L30 20 L265 20 L270 60 L270 143"/>
  <path class="cut" d="M270 143 L274 26 L282 20 L755 20 L762 26 L762 143"/>
  <path class="cut" d="M762 143 L765 60 L765 20 L1000 20 L1007 60 L1007 143"/>
  <path class="cut" d="M1007 143 L1011 26 L1019 20 L1473 20 L1480 26 L1480 143"/>

  <!-- Bottom flaps -->
  <path class="cut" d="M28 390 L30 470 L30 512 L265 512 L270 470 L270 390"/>
  <path class="cut" d="M270 390 L274 505 L282 512 L755 512 L762 505 L762 390"/>
  <path class="cut" d="M762 390 L765 470 L765 512 L1000 512 L1007 470 L1007 390"/>
  <path class="cut" d="M1007 390 L1011 505 L1019 512 L1473 512 L1480 505 L1480 390"/>

  <!-- Side panel (narrow) -->
  <g class="panel-side">
    <rect class="band-gold" x="28" y="143" width="242" height="247"/>
    <rect x="38" y="208" width="140" height="150" fill="url(#quiltTone)" role="img" aria-label="Photo of a white baffle-box down comforter"/>
    <polygon class="band-lemon" points="195,143 270,143 270,390 197,390 130,265"/>
    <polygon class="chevron-ink" points="183,143 195,143 130,265 197,390 180,390 116,265"/>
    <circle class="brand-mark" cx="76" cy="172" r="9"/>
    <text class="brand-name" x="76" y="195" text-anchor="middle">LOFTWELL</text>
    <text class="company-field" x="181" y="260">Company</text>
    <text class="company-field" x="181" y="272">Name………</text>
    <text class="company-field" x="181" y="284">Address…….</text>
  </g>

  <!-- Front panel (wide) -->
  <g class="panel-front">
    <rect class="band-gold" x="270" y="143" width="492" height="247"/>
    <rect x="393" y="168" width="220" height="194" fill="url(#quiltTone)" role="img" aria-label="Photo of a white baffle-box down comforter"/>
    <polygon class="band-lemon" points="660,143 762,143 762,390 660,390 598,262"/>
    <polygon class="chevron-ink" points="645,143 660,143 598,262 660,390 645,390 582,262"/>
    <circle class="brand-mark" cx="333" cy="188" r="11"/>
    <text class="brand-name" x="333" y="215" text-anchor="middle">LOFTWELL</text>
    <text class="origin-note" x="333" y="319" text-anchor="middle">The product</text>
    <text class="origin-note" x="333" y="330" text-anchor="middle">is DESIGNED</text>
    <text class="origin-note" x="333" y="342" text-anchor="middle">IN AUSTRALIA</text>
    <foreignObject x="635" y="200" width="121" height="130">
      <p xmlns="http://www.w3.org/1999/xhtml" class="story">Down is a natural material and the higher the Down content, the lighter and softer the product. Down differs considerably from feathers, as it does not have the hard quill shafts that is common to feather. It is the fluffy filament which comes from the breast of a duck and is an extremely efficient natural insulator.</p>
    </foreignObject>
  </g>

  <!-- Side panel (narrow, repeat) -->
  <g class="panel-side" transform="translate(734 0)">
    <rect class="band-gold" x="28" y="143" width="245" height="247"/>
    <rect x="38" y="208" width="140" height="150" fill="url(#quiltTone)" role="img" aria-label="Photo of a white baffle-box down comforter"/>
    <polygon class="band-lemon" points="195,143 273,143 273,390 197,390 130,265"/>
    <polygon class="chevron-ink" points="183,143 195,143 130,265 197,390 180,390 116,265"/>
    <circle class="brand-mark" cx="76" cy="172" r="9"/>
    <text class="brand-name" x="76" y="195" text-anchor="middle">LOFTWELL</text>
    <text class="company-field" x="181" y="260">Company</text>
    <text class="company-field" x="181" y="272">Name………</text>
    <text class="company-field" x="181" y="284">Address…….</text>
  </g>

  <!-- Back panel (wide, repeat) -->
  <g class="panel-front" transform="translate(737 0)">
    <rect class="band-gold" x="270" y="143" width="473" height="247"/>
    <rect x="393" y="168" width="220" height="194" fill="url(#quiltTone)" role="img" aria-label="Photo of a white baffle-box down comforter"/>
    <polygon class="band-lemon" points="660,143 743,143 743,390 660,390 598,262"/>
    <polygon class="chevron-ink" points="645,143 660,143 598,262 660,390 645,390 582,262"/>
    <circle class="brand-mark" cx="333" cy="188" r="11"/>
    <text class="brand-name" x="333" y="215" text-anchor="middle">LOFTWELL</text>
    <text class="origin-note" x="333" y="319" text-anchor="middle">The product</text>
    <text class="origin-note" x="333" y="330" text-anchor="middle">is DESIGNED</text>
    <text class="origin-note" x="333" y="342" text-anchor="middle">IN AUSTRALIA</text>
    <foreignObject x="635" y="200" width="106" height="135">
      <p xmlns="http://www.w3.org/1999/xhtml" class="story">Down is a natural material and the higher the Down content, the lighter and softer the product. Down differs considerably from feathers, as it does not have the hard quill shafts that is common to feather. It is the fluffy filament which comes from the breast of a duck and is an extremely efficient natural insulator.</p>
    </foreignObject>
  </g>

  <!-- Fold lines and band edges -->
  <line class="cut" x1="4" y1="143" x2="1480" y2="143"/>
  <line class="cut" x1="4" y1="390" x2="1480" y2="390"/>
  <line class="cut" x1="28" y1="143" x2="28" y2="390"/>
  <line class="cut" x1="270" y1="143" x2="270" y2="390"/>
  <line class="cut" x1="762" y1="143" x2="762" y2="390"/>
  <line class="cut" x1="1007" y1="143" x2="1007" y2="390"/>
  <line class="cut" x1="1480" y1="143" x2="1480" y2="390"/>
</svg>
</body>
</html>
```